The Hearthstone

We need a menu design for our restaurant. Our current menu was designed by us and is ok - but we would like something more... The current lay out is in a tri-fold 8x11 - we want to keep the to a standard paper size but would like to make it larger so the menu items stand out more (maybe double sided 6x11 or double sided 8x11). Ideally, we'd like to have a design where we can edit the text accordingly, as our menu choices change regularly. The feel of the restaurant is casual and rustic. We specialize in Craft Beers, Wings and Burritos - everything is homemade and made fresh daily - we'd like the menu to be more 'user friendly'. Our Burritos are made to order. A customer chooses their meat then adds toppings. Because of our currently lay out - descriptions are small and flow is not great. I'd also like to add some appropriate graphics to make it more appealing. We are in family restaurant in a resort town and cater to skiers, mountain bikers, hikers hunters, fisherman, ect...the atmosphere is casual, eclectic, and rustic with a bit of a "hippy" vibe for lack of better term. Always good music, good food, good times...
Target Market(s)
We cater to Locals (hunters/country/"simple folk") AND Tourists (hipster "city slickers") who visit the area. We have a niche where we successfully cater to both because we are not too much one or the other. We are relatable to both and the menu feel should reflect the same.
Industry/Entity Type
Restaurant
Requirements
Must have
- Text of file must be editable by us once final design is received. We need to be able to update the text of menu accordingly.
- Hearthstone logo.
Nice to have
- More graphics, better fonts (fonts should be fun/casual)

```html
<!DOCTYPE html>
<html lang="en">
<head>
<meta charset="utf-8">
<title>The Hearthstone – Menu</title>
<link rel="stylesheet" href="https://fonts.googleapis.com/css2?family=Oleo+Script:wght@700&family=Roboto:wght@400;500;700;900&family=Roboto+Slab:wght@700&family=Lora:ital,wght@1,500&display=swap">
<style>
  :root{
    --paper:#f1f1f0;
    --paper-edge:#e3e3e1;
    --brown:#8a5a2b;
    --ink:#1f1f1f;
    --red:#c9201f;
    --orange:#e8691f;
    --leaf-red:#c7301d;
    --leaf-orange:#ea8a1e;
    --leaf-green:#2f6a2a;
  }
  html,body{margin:0;padding:0;overflow:hidden;background:#fff;}
  .menu{
    position:relative;width:848px;height:1200px;overflow:hidden;
    background:linear-gradient(90deg,var(--paper) 0%,#f7f7f6 45%,var(--paper-edge) 100%);
    font-family:"Roboto",Arial,sans-serif;color:var(--ink);
  }
  .abs{position:absolute;}
  .leaves{position:absolute;}
  .leaves-top-left{left:0;top:0;width:150px;height:50px;border-radius:0 0 60px 0;background:linear-gradient(120deg,var(--leaf-orange),var(--leaf-green) 60%,var(--leaf-red));opacity:.85;}
  .leaves-top-mid{left:300px;top:0;width:60px;height:24px;border-radius:0 0 34px 34px;background:linear-gradient(90deg,var(--leaf-orange),var(--leaf-green));opacity:.8;}
  .leaves-top-right{right:0;top:0;width:96px;height:160px;border-radius:0 0 0 80px;background:linear-gradient(200deg,var(--leaf-red),var(--leaf-orange) 50%,var(--leaf-green));opacity:.85;}
  .leaves-bottom-left{left:0;bottom:0;width:56px;height:70px;border-radius:0 56px 0 0;background:linear-gradient(30deg,var(--leaf-green),var(--leaf-orange));opacity:.85;}
  .leaves-bottom-right{right:0;bottom:0;width:28px;height:36px;border-radius:30px 0 0 0;background:linear-gradient(0deg,var(--leaf-orange),var(--leaf-red));opacity:.8;}
  .food-photo{left:164px;top:1106px;width:258px;height:94px;border-radius:50px 50px 0 0;background:radial-gradient(ellipse at 50% 60%,#c4622a 0%,#a8461c 45%,#7fa64a 80%,#e9e9e6 100%);}

  .brand{left:31px;width:360px;top:150px;text-align:center;font-family:"Roboto Slab",Georgia,serif;font-weight:700;font-size:30px;color:var(--brown);text-transform:uppercase;white-space:nowrap;}
  .hours-title{left:31px;width:360px;top:244px;text-align:center;font-weight:700;font-size:17px;color:var(--brown);}
  .hours-line{left:31px;width:360px;text-align:center;font-size:18px;font-weight:500;color:var(--ink);}
  .hours-time{color:var(--brown);}

  .section-title{position:absolute;font-family:"Oleo Script",Georgia,cursive;font-weight:700;font-size:28px;color:var(--brown);}
  .sub-title{position:absolute;font-size:18px;font-weight:500;}
  .dots{position:absolute;height:0;border-top:2px dotted var(--brown);}
  .dots.double{height:3px;border-bottom:2px dotted var(--brown);}
  .col-left{left:31px;width:360px;}
  .col-right{left:456px;width:368px;}

  .row{position:absolute;display:flex;justify-content:space-between;font-size:13px;font-weight:500;}
  .row.big{font-size:18px;}
  .level{position:absolute;font-size:12.5px;}
  .level b{color:var(--brown);font-weight:700;}
  .desc{position:absolute;font-family:"Lora",Georgia,serif;font-style:italic;font-weight:500;font-size:12.5px;line-height:16px;color:var(--brown);}

  .banner{position:absolute;left:50px;width:323px;box-sizing:border-box;border:2px solid var(--brown);border-radius:14px;outline:1px solid var(--brown);outline-offset:3px;text-align:center;font-family:"Lora",Georgia,serif;font-style:italic;font-weight:500;color:var(--brown);background:var(--paper);}
  .banner-sauces{top:624px;height:38px;line-height:34px;font-size:21px;}
  .banner-sides{top:794px;height:46px;padding-top:3px;font-size:17px;line-height:19px;}

  .center-note{position:absolute;left:31px;width:360px;text-align:center;}

  .happy{left:418px;top:12px;font-size:20px;line-height:24px;color:var(--red);}
  .red-bar{position:absolute;height:5px;background:var(--red);}
  .get-some{left:404px;top:46px;font-weight:900;font-size:46px;line-height:50px;color:var(--red);}
  .wing-night{left:408px;top:102px;font-size:27px;line-height:32px;color:var(--orange);}
  .thursday{left:408px;top:136px;font-size:27px;line-height:32px;color:var(--orange);}
  .thursday i{font-family:"Lora",Georgia,serif;color:var(--red);}

  .topping{position:absolute;font-size:13px;font-weight:500;}
  .topping-note{position:absolute;font-family:"Lora",Georgia,serif;font-style:italic;font-size:12.5px;color:var(--brown);}
  .divider{position:absolute;left:631px;top:416px;width:2px;height:148px;background:var(--brown);}
</style>
</head>
<body>
<main class="menu">
  <div class="leaves leaves-top-left" role="img" aria-label="Autumn leaves decoration"></div>
  <div class="leaves leaves-top-mid" role="img" aria-label="Autumn leaves decoration"></div>
  <div class="leaves leaves-top-right" role="img" aria-label="Autumn leaves decoration"></div>
  <div class="leaves leaves-bottom-left" role="img" aria-label="Autumn leaves decoration"></div>
  <div class="leaves leaves-bottom-right" role="img" aria-label="Autumn leaves decoration"></div>
  <div class="abs food-photo" role="img" aria-label="Photo of chicken wings with salad garnish on a plate"></div>

  <div class="abs brand">The Hearthstone</div>
  <div class="abs hours-title">Open Hours</div>
  <div class="abs hours-line" style="top:268px">Thurs, Friday &amp; Saturday</div>
  <div class="abs hours-line hours-time" style="top:288px">4 p.m &nbsp;to 12 a.m.</div>

  <div class="section-title" style="left:31px;top:310px">Wings</div>
  <div class="dots double col-left" style="top:348px"></div>
  <div class="row big col-left" style="top:366px"><span>Buffalo Style</span><span>$9.00</span></div>
  <div class="dots col-left" style="top:396px"></div>
  <div class="level" style="left:31px;top:402px"><b>Mild:</b> Sweet &amp; Tangy</div>
  <div class="level" style="left:31px;top:419px"><b>Medium:</b> Bold &nbsp;&amp; Spicy</div>
  <div class="level" style="left:31px;top:436px"><b>Hot:</b> Teary-Eyed &amp; Sweaty-Browed</div>

  <div class="sub-title" style="left:31px;top:466px">Specialty</div>
  <div class="dots col-left" style="top:496px"></div>
  <div class="row col-left" style="top:508px"><span>BBQ</span><span>$9.00</span></div>
  <div class="row col-left" style="top:530px"><span>Ha-B-Q (hot!)</span><span>$11.00</span></div>
  <div class="row col-left" style="top:552px"><span>Shanghai Garlic</span><span>$11.00</span></div>
  <div class="row col-left" style="top:574px"><span>Hot Honey Thai</span><span>$11.00</span></div>
  <div class="row col-left" style="top:596px"><span>RazbaNero (hot!)</span><span>$11.00</span></div>

  <div class="banner banner-sauces">All Sauces Are Homemade!</div>

  <div class="sub-title" style="left:31px;top:682px">Sampler</div>
  <div class="dots col-left" style="top:710px"></div>
  <div class="row col-left" style="top:722px"><span>Dozen wings</span><span>$15.00</span></div>
  <div class="desc" style="left:31px;top:737px">Mix and match<br>Your choice of 3 flavors (4 wings ea.)</div>

  <div class="banner banner-sides">All wings are served with Blue<br>Cheese or Ranch, Celery &nbsp;&amp; Carrots</div>

  <div class="section-title" style="left:31px;top:876px">Burritos</div>
  <div class="dots double col-left" style="top:916px"></div>
  <div class="center-note" style="top:931px;font-size:13px;font-weight:500">Build your own!</div>
  <div class="center-note" style="top:947px;font-size:12px">Includes choice of meat, toppings &amp; side of salsa and chips</div>
  <div class="center-note desc" style="top:962px;font-size:17px;line-height:20px">All Ingredients made fresh daily!</div>

  <div class="sub-title" style="left:31px;top:992px">Meats</div>
  <div class="dots col-left" style="top:1020px"></div>
  <div class="row col-left" style="top:1034px"><span>Red Chile Grilled Chicken</span><span>$9.00</span></div>
  <div class="desc" style="left:31px;top:1050px;width:360px">ChickenMarinated in a Red Chile Ancho sauce – this grilled chicken is the perfect blend of sassy, salty, savory and mild spice</div>

  <div class="abs happy">Happy Hour Specials</div>
  <div class="red-bar" style="left:404px;top:40px;width:300px"></div>
  <div class="abs get-some">Get Some...</div>
  <div class="red-bar" style="left:404px;top:97px;width:300px"></div>
  <div class="abs wing-night">Wing Night Specials</div>
  <div class="abs thursday">Every <i>Thursday</i></div>

  <div class="row col-right" style="top:194px"><span>Spicy Shredded Beef</span><span>$9.00</span></div>
  <div class="desc" style="left:456px;top:210px;width:370px">Slow cooked in a Chipotle Pepper sauce – saucy &amp; spicy</div>
  <div class="row col-right" style="top:240px"><span>Pork Carnitas</span><span>$9.00</span></div>
  <div class="desc" style="left:456px;top:256px;width:368px">Wrapped in bacon and slow roasted – our pork is seasoned to perfection with subtle hints of clove and citrus</div>
  <div class="row col-right" style="top:305px"><span>Veggie</span><span>$9.00</span></div>
  <div class="desc" style="left:456px;top:321px;width:372px">Wrap up your favorite combination of meat-free toppings to create a vegetarian delight (guac included)</div>

  <div class="sub-title" style="left:456px;top:366px">Personalize</div>
  <div class="dots col-right" style="top:396px"></div>
  <div class="topping" style="left:456px;top:414px">Cheddar Jack Cheese</div>
  <div class="topping" style="left:456px;top:438px">Sour Cream</div>
  <div class="topping" style="left:456px;top:463px">Black Beans</div>
  <div class="topping" style="left:456px;top:488px">Refried Beans</div>
  <div class="topping" style="left:456px;top:512px">Cilantro Lime Rice</div>
  <div class="topping" style="left:456px;top:536px">Guacamole</div>
  <div class="topping-note" style="left:456px;top:552px">(add $1.00)</div>
  <div class="divider"></div>
  <div class="topping" style="left:691px;top:414px">Red Onion</div>
  <div class="topping" style="left:691px;top:440px">Bacon</div>
  <div class="topping" style="left:691px;top:464px">Medium Salsa</div>
  <div class="topping" style="left:691px;top:489px">Pico de Gallo</div>
  <div class="topping-note" style="left:691px;top:506px">(mild tomato salsa)</div>
  <div class="topping" style="left:691px;top:531px">Hot Salsa</div>
  <div class="topping" style="left:691px;top:552px">Lettuce</div>

  <div class="section-title" style="left:456px;top:574px">Extras</div>
  <div class="dots double col-right" style="top:612px"></div>
  <div class="row col-right" style="top:629px"><span>Basket of Chips &amp; Salsa</span><span>$4.00</span></div>
  <div class="row col-right" style="top:654px"><span>Basket of Chips &amp; Guacamole</span><span>$4.00</span></div>
  <div class="row col-right" style="top:679px"><span>Basket of Steak Fries</span><span>$4.00</span></div>
  <div class="row col-right" style="top:704px"><span>Kids Basket of Fries &amp; Nuggets</span><span>$5.00</span></div>
  <div class="row col-right" style="top:729px"><span>Deep Fried Smore</span><span>$3.00</span></div>

  <div class="section-title" style="left:456px;top:760px">Drinks</div>
  <div class="dots double col-right" style="top:800px"></div>
  <div class="row col-right" style="top:820px"><span>Cola</span><span>$3.00</span></div>
  <div class="row col-right" style="top:843px"><span>Diet Cola</span><span>$3.00</span></div>
  <div class="row col-right" style="top:865px"><span>Lemon-Lime Soda</span><span>$3.00</span></div>
  <div class="row col-right" style="top:888px"><span>Ginger Ale</span><span>$3.00</span></div>
  <div class="row col-right" style="top:910px"><span>Citrus Soda</span><span>$3.00</span></div>
  <div class="row col-right" style="top:933px"><span>Cherry Fizz</span><span>$3.00</span></div>
  <div class="row col-right" style="top:955px"><span>Iced Tea</span><span>$3.00</span></div>
  <div class="row col-right" style="top:978px"><span>Sweet Tea</span><span>$3.00</span></div>
  <div class="row col-right" style="top:1001px"><span>Kids Milk</span><span>$1.50</span></div>
  <div class="row col-right" style="top:1023px"><span>Kids Cranberry Juice</span><span>$1.50</span></div>
  <div class="row col-right" style="top:1046px"><span>Kids Apple Juice</span><span>$1.50</span></div>
  <div class="row col-right" style="top:1068px"><span>Kids Soda</span><span>$1.50</span></div>
  <div class="row col-right" style="top:1091px"><span>Coffee</span><span>$1.50</span></div>
  <div class="row col-right" style="top:1113px"><span>Hot Tea</span><span>$1.50</span></div>
  <div class="row col-right" style="top:1136px"><span>Hot Chocolate</span><span>$1.50</span></div>
</main>
</body>
</html>
```